.

Target Market(s)

Young, male, tech savvy, cryptocurrency investors

Industry/Entity Type

Information Technology

Logo Text

.

Coding

Coded - Design and coding required

Number of Pages Required

1 page

Font styles to use
Sans Serif

Colors

Designer to choose colors to be used in the design.

Requirements
Must have
• .

```html
<!DOCTYPE html>
<html lang="en">
<head>
<meta charset="utf-8">
<title>Kryon.network — Proof-of-Individuality Human Airdrop</title>
<link rel="stylesheet" href="https://fonts.googleapis.com/css2?family=Open+Sans:ital,wght@0,400;0,600;0,700;1,400;1,700&display=swap">
<style>
  :root {
    --brand-blue: #1f2f9e;
    --brand-orange: #f26a10;
    --hero-deep: #1b73c6;
    --hero-mid: #5aa6de;
    --hero-light: #c7e2f4;
    --text-dark: #222;
    --text-grey: #666;
    --bezel: #1a1a1a;
    --white: #fff;
  }
  * { box-sizing: border-box; margin: 0; padding: 0; }
  html, body { width: 968px; height: 1200px; overflow: hidden; background: var(--white); }
  body { font-family: "Open Sans", Arial, sans-serif; color: var(--text-dark); position: relative; }

  .site-header { position: absolute; top: 0; left: 0; width: 968px; height: 170px; }
  .brand { position: absolute; left: 30px; top: 32px; display: flex; align-items: center; gap: 14px; }
  .brand-mark { width: 44px; height: 44px; border-radius: 50%; background: var(--brand-orange); }
  .brand-name { font-size: 50px; font-weight: 700; color: var(--brand-blue); line-height: 1; letter-spacing: -0.5px; }
  .tagline { position: absolute; right: 40px; top: 40px; text-align: center; font-size: 19px; font-weight: 700; font-style: italic; color: var(--text-grey); line-height: 1.4; }

  .hero { position: absolute; top: 170px; left: 0; width: 968px; height: 544px; overflow: hidden;
    background: linear-gradient(100deg, var(--hero-light) 0%, var(--hero-mid) 45%, var(--hero-deep) 100%); }
  .hero-photo { position: absolute; inset: 0; }
  .hero-title { position: absolute; top: 30px; width: 100%; text-align: center; color: var(--white); font-size: 52px; font-weight: 400; line-height: 1.3; }
  .hero-subtitle { position: absolute; top: 100px; width: 100%; text-align: center; color: var(--white); font-size: 32px; font-weight: 400; line-height: 1.3; }
  .hero-arrow { position: absolute; top: 255px; }
  .hero-arrow.prev { left: 18px; }
  .hero-arrow.next { right: 18px; }

  .feature-strip { position: absolute; top: 423px; left: 0; width: 968px; height: 110px; }
  .feature-screen { position: absolute; top: 0; height: 110px; background: var(--bezel); border-radius: 6px; padding: 7px; }
  .feature-screen .screen { width: 100%; height: 100%; background: linear-gradient(180deg, #3f9fe6, #2a7fd0); }
  .slider-dots { position: absolute; top: 473px; left: 420px; display: flex; gap: 31px; }
  .dot { width: 22px; height: 22px; border-radius: 50%; background: var(--brand-orange); border: 2px solid #ccc; }
  .dot.active { background: var(--white); }

  .about { position: absolute; top: 748px; left: 36px; width: 896px; }
  .about h2 { text-align: center; color: var(--brand-blue); font-size: 31px; font-weight: 700; line-height: 1.3; margin-bottom: 18px; }
  .about p { font-size: 20.8px; line-height: 35.5px; }

  .signup { position: absolute; top: 1106px; left: 36px; width: 866px; height: 60px; display: flex; align-items: center; }
  .signup-label { color: var(--brand-blue); font-size: 27px; font-weight: 700; width: 187px; white-space: nowrap; }
  .signup-input { width: 430px; height: 60px; border: 2px solid #bbb; padding: 0 18px; display: flex; align-items: center; font-style: italic; font-size: 19px; color: #444; }
  .signup-button { margin-left: 25px; width: 224px; height: 60px; background: var(--brand-orange); color: var(--white); font-size: 26px; font-weight: 600; display: flex; align-items: center; justify-content: center; }
</style>
</head>
<body>
  <header class="site-header">
    <div class="brand">
      <span class="brand-mark"></span>
      <span class="brand-name">Kryon.network</span>
    </div>
    <div class="tagline">The World's Most Advanced Blockchain and<br>the Widest Token Distribution</div>
  </header>

  <section class="hero">
    <div class="hero-photo" role="img" aria-label="Photo of a person wearing blue glasses in front of a blue background of binary code"></div>
    <h1 class="hero-title">November 2017</h1>
    <p class="hero-subtitle">Proof-of-Individuality Human Airdrop</p>
    <svg class="hero-arrow prev" width="24" height="34" viewBox="0 0 24 34"><polygon points="22,2 2,17 22,32" fill="#fff"/></svg>
    <svg class="hero-arrow next" width="24" height="34" viewBox="0 0 24 34"><polygon points="2,2 22,17 2,32" fill="#fff"/></svg>

    <div class="feature-strip">
      <div class="feature-screen" style="left:53px;width:208px;"><div class="screen" role="img" aria-label="Illustration of a group of people with a speech bubble"></div></div>
      <div class="feature-screen" style="left:281px;width:213px;"><div class="screen" role="img" aria-label="Illustration of a family"></div></div>
      <div class="feature-screen" style="left:508px;width:199px;"><div class="screen" role="img" aria-label="Illustration of a support agent with headset"></div></div>
      <div class="feature-screen" style="left:726px;width:213px;"><div class="screen" role="img" aria-label="Illustration of a wifi sign"></div></div>
    </div>
    <div class="slider-dots">
      <span class="dot"></span><span class="dot"></span><span class="dot active"></span>
    </div>
  </section>

  <section class="about">
    <h2>About Kryon Network</h2>
    <p>Lorem Ipsum is simply dummy text of the printing and typesetting industry. Lorem Ipsum has been the industry's standard dummy text ever since the 1500s, when an unknown printer took a galley of type and scrambled it to make a type specimen book. It has survived not only five centuries, but also the leap into electronic typesetting, remaining essentially unchanged. It was popularised in the 1960s with the release of Quillmark sheets containing Lorem Ipsum passages, and more recently with desktop publishing software like Pressline Studio including versions of Lorem Ipsum.</p>
  </section>

  <form class="signup">
    <span class="signup-label">Get Updates:</span>
    <span class="signup-input">Your email</span>
    <span class="signup-button">Sign-up Now</span>
  </form>
</body>
</html>
```